Business card design needed

New company based in Brisbane, Australia. Brindle Systems. The business is focused on the delivery of network architecture design and deployment. We will provide both services and the sale of the necessary equipment to deliver the service. Cloud computing is an important element of our focus as this is an emerging market for enterprises in Queensland. Our target marketplace is medium to large corporations with complex infrastructure requirements. IT Management and above will be the typical entry point for us into these accounts. We would like to see the use of various shade of green, design should be clutter free and impress stability, trust and growth.
Updates
Hey Everyone
Just we let you all know we have changed this project to 'committed' payment status.
Looking forward to seeing the designs! Thanks for your efforts.
Best Regards
Marcus
Industry/Entity Type
Architecture
Contact Information for Business Card
Brindle Systems, Marcus Doyle, Sales Director, Level 14 Harlow Tower, 58 Penfold Street, Brisbane QLD 4000, Ph +61 7 3904 2267, M +61 4 4926 1573, E marcus.doyle@brindlesystems-example.com.au
Look and feel
Each slider illustrates characteristics of the customer's brand and the style your logo design should communicate.

```html
<!DOCTYPE html>
<html lang="en">
<head>
<meta charset="utf-8">
<title>Brindle Systems – Business Card</title>
<link href="https://fonts.googleapis.com/css2?family=Michroma&display=swap" rel="stylesheet">
<style>
  :root {
    --page-bg: #e9ebee;
    --card-bg: #ffffff;
    --brand-blue: #2a5caa;
    --brand-green: #3aa53c;
    --deco-blue: #2f63b8;
    --deco-green: #34a846;
    --card-shadow: rgba(20, 30, 45, 0.18);
  }
  * { margin: 0; padding: 0; box-sizing: border-box; }
  html, body {
    width: 1200px; height: 900px; overflow: hidden;
    background: var(--page-bg);
    font-family: "Michroma", sans-serif;
  }
  .stage { position: relative; width: 1200px; height: 900px; }

  .card {
    position: absolute;
    width: 560px; height: 320px;
    background: var(--card-bg);
    border-radius: 22px;
    box-shadow: 0 10px 30px var(--card-shadow);
    overflow: hidden;
  }
  .card-front { left: 70px; top: 70px; }
  .card-back { left: 570px; top: 500px; }

  /* Shared wordmark */
  .wordmark {
    position: absolute;
    display: flex; align-items: center; gap: 10px;
  }
  .wordmark-square {
    flex: none;
    width: 16px; height: 16px; background: var(--brand-blue);
  }
  .wordmark-name {
    display: flex; flex-direction: column;
    color: var(--brand-blue);
    font-size: 14px;
    line-height: 1.25;
    letter-spacing: 2px;
    text-transform: uppercase;
  }

  /* Front */
  .front-decoration {
    position: absolute; left: 0; top: 96px;
    width: 330px; height: 200px;
    background: linear-gradient(135deg, var(--deco-blue) 0%, var(--deco-blue) 45%, var(--deco-green) 55%, var(--deco-green) 100%);
    opacity: 0.85;
    border-radius: 0 6px 6px 0;
  }
  .front-wordmark { right: 30px; top: 56px; }

  /* Back */
  .back-bands { position: absolute; inset: 0; }
  .back-wordmark { right: 34px; top: 34px; }

  .contact-name {
    position: absolute; left: 50px; top: 112px;
    color: var(--brand-blue);
    font-size: 14px; letter-spacing: 1px;
    font-variant: small-caps;
  }
  .contact-title {
    position: absolute; left: 120px; top: 136px;
    color: var(--brand-green);
    font-size: 10px; letter-spacing: 1px;
    font-variant: small-caps;
  }
  .contact-line {
    position: absolute;
    display: flex; align-items: center; gap: 8px;
    font-size: 12px; letter-spacing: 1.5px;
    color: var(--brand-blue);
    white-space: nowrap;
  }
  .contact-line svg { flex: none; }
  .contact-phone { left: 320px; top: 176px; }
  .contact-mobile { left: 36px; top: 236px; }
  .contact-email { left: 36px; top: 266px; font-size: 10px; letter-spacing: 1px; }
  .contact-address {
    left: 36px; top: 292px; font-size: 8.5px; letter-spacing: 1px;
    color: var(--brand-green); font-variant: small-caps;
  }
</style>
</head>
<body>
<main class="stage">

  <section class="card card-front" aria-label="Card front">
    <div class="front-decoration" role="img" aria-label="Large blue and green brand decoration"></div>
    <div class="wordmark front-wordmark">
      <span class="wordmark-square"></span>
      <span class="wordmark-name"><span>Brindle</span><span>Systems</span></span>
    </div>
  </section>

  <section class="card card-back" aria-label="Card back">
    <svg class="back-bands" width="560" height="320" viewBox="0 0 560 320" aria-hidden="true">
      <polygon points="0,212 262,150 270,156 0,222" fill="var(--brand-blue)"/>
      <polygon points="292,152 560,92 560,101 300,158" fill="var(--brand-green)"/>
    </svg>

    <div class="wordmark back-wordmark">
      <span class="wordmark-square"></span>
      <span class="wordmark-name"><span>Brindle</span><span>Systems</span></span>
    </div>

    <p class="contact-name">Marcus Doyle</p>
    <p class="contact-title">Sales Director</p>

    <p class="contact-line contact-phone">
      <svg width="14" height="14" viewBox="0 0 14 14" aria-hidden="true">
        <circle cx="7" cy="7" r="6" fill="none" stroke="var(--brand-green)" stroke-width="1.3"/>
        <path d="M5 4.2 L6.2 5.6 L5.6 6.3 Q6.6 8 7.8 8.5 L8.5 7.9 L9.8 9 L9 10 Q6 10 4.2 5.3 Z" fill="var(--brand-green)"/>
      </svg>
      +61 7 3904 2267
    </p>
    <p class="contact-line contact-mobile">
      <svg width="10" height="15" viewBox="0 0 10 15" aria-hidden="true">
        <rect x="1" y="1" width="8" height="13" rx="1.5" fill="none" stroke="var(--brand-green)" stroke-width="1.3"/>
        <line x1="4" y1="12" x2="6" y2="12" stroke="var(--brand-green)" stroke-width="1.2"/>
      </svg>
      +61 4 4926 1573
    </p>
    <p class="contact-line contact-email">marcus.doyle@brindlesystems-example.com.au</p>
    <p class="contact-line contact-address">Level 14 Harlow Tower, 58 Penfold Street, Brisbane QLD 4000</p>
  </section>

</main>
</body>
</html>
```